Apartment services app

The app should permit current residents to pay rent, submit work orders or submit comments and general requests. There is an app that is available from Heron Works in the UK that could be used to benchmark, but I would like to see something more appropriate for the US.
Updates

The company name for this project is Oakvale Property Management. We will be providing a logo at a later date as we we will be submitting a separate design project for the development of a new logo.

Reason: I am extending the deadline by another week so that I may comment on the designs so far and each of you will have time to respond Tim

Target Market(s)

Residents of our apartment communities

Industry/Entity Type

Apartment

Requirements
Must have
• Ability to pay rent
• Ability to have reminders sent to resident
• Notices sent to resident
• Resident able to submit work order requests
• Resident able to submit comments and complaints

```html
<!DOCTYPE html>
<html lang="en">
<head>
<meta charset="utf-8">
<title>Oakvale Property Management – Report</title>
<link rel="stylesheet" href="https://fonts.googleapis.com/css2?family=Open+Sans:wght@300;400;600&display=swap">
<style>
  :root {
    --canvas: #2b2d31;
    --bar-dark: #55585e;
    --bar-mid: #62656c;
    --panel: #6a6d74;
    --card: #ffffff;
    --card-edge: #e6e6e6;
    --ink: #3a3a3a;
    --ink-soft: #8a8a8a;
    --rule: #dcdcdc;
    --accent: #e04a4a;
    --on-dark: #e9eaec;
    --on-dark-soft: #b9bbc0;
  }
  * { box-sizing: border-box; margin: 0; padding: 0; }
  html, body { width: 1200px; height: 892px; overflow: hidden; }
  body {
    background: var(--canvas);
    font-family: "Open Sans", Arial, sans-serif;
    position: relative;
  }
  .screen {
    position: absolute; left: 360px; top: 20px;
    width: 480px; height: 852px;
    background: var(--panel);
    overflow: hidden;
  }
  .status-bar {
    height: 30px; background: var(--bar-dark);
    display: flex; align-items: center; justify-content: space-between;
    padding: 0 12px; color: var(--on-dark);
    font-size: 15px; font-weight: 600;
  }
  .status-bar .carrier { display: flex; align-items: center; gap: 6px; }
  .status-bar .battery { display: flex; align-items: center; gap: 6px; }
  .app-header {
    height: 58px; background: var(--bar-mid);
    display: flex; align-items: center; justify-content: space-between;
    padding: 0 18px; color: var(--on-dark);
  }
  .app-header .title { font-size: 19px; font-weight: 400; }
  .report-card {
    position: absolute; left: 18px; right: 18px; top: 100px; height: 622px;
    background: var(--card); border: 3px solid var(--card-edge);
    padding: 30px 30px 0;
    color: var(--ink);
  }
  .card-heading { display: flex; align-items: center; gap: 18px; }
  .card-heading h1 { font-size: 21px; font-weight: 400; letter-spacing: .3px; }
  .rule { height: 1px; background: var(--rule); margin: 20px 0 14px; }
  .complaint { font-size: 18px; line-height: 1.25; font-weight: 400; margin-bottom: 18px; }
  .body-copy p { font-size: 10.5px; line-height: 1.6; color: var(--ink-soft); margin-bottom: 10px; }
  .submit-button {
    display: block; width: 178px; height: 36px; margin-top: 24px;
    background: var(--accent); color: #fff; border: 0;
    font: 400 14px "Open Sans", Arial, sans-serif;
  }
  .tab-bar {
    position: absolute; left: 0; right: 0; bottom: 0; height: 112px;
    background: var(--bar-dark);
    display: grid; grid-template-columns: repeat(4, 1fr);
  }
  .tab {
    display: flex; flex-direction: column; align-items: center; justify-content: center;
    gap: 8px; color: var(--on-dark-soft); font-size: 13px;
    border-right: 1px solid #4a4d53;
  }
  .tab:last-child { border-right: 0; }
  .tab svg { stroke: var(--on-dark-soft); fill: none; stroke-width: 1.6; }
</style>
</head>
<body>
<main class="screen">
  <div class="status-bar">
    <span class="carrier">
      <svg width="22" height="12" viewBox="0 0 22 12" fill="#e9eaec"><rect x="0" y="8" width="3" height="4"/><rect x="4.5" y="6" width="3" height="6"/><rect x="9" y="4" width="3" height="8"/><rect x="13.5" y="2" width="3" height="10"/><rect x="18" y="0" width="3" height="12"/></svg>
      KESTREL
    </span>
    <span class="time">10:35 AM</span>
    <span class="battery">
      <svg width="12" height="12" viewBox="0 0 12 12"><circle cx="6" cy="6" r="5.5" fill="#e9eaec"/><path d="M6 3v3h2" stroke="#55585e" stroke-width="1.4" fill="none"/></svg>
      65 %
      <svg width="28" height="13" viewBox="0 0 28 13"><rect x="0.5" y="0.5" width="24" height="12" rx="2" fill="none" stroke="#e9eaec"/><rect x="2.5" y="2.5" width="14" height="8" fill="#e9eaec"/><rect x="25.5" y="4" width="2" height="5" fill="#e9eaec"/></svg>
    </span>
  </div>

  <header class="app-header">
    <svg class="icon-settings" width="24" height="24" viewBox="0 0 24 24" fill="none" stroke="#b9bbc0" stroke-width="1.5"><circle cx="12" cy="12" r="3.5"/><path d="M12 2v3M12 19v3M2 12h3M19 12h3M4.9 4.9l2.1 2.1M17 17l2.1 2.1M4.9 19.1L7 17M17 7l2.1-2.1"/></svg>
    <span class="title">Report</span>
    <svg class="icon-help" width="26" height="26" viewBox="0 0 26 26"><circle cx="13" cy="13" r="11.5" fill="none" stroke="#b9bbc0" stroke-width="1.4"/><text x="13" y="18" text-anchor="middle" font-family="Open Sans, sans-serif" font-size="13" fill="#b9bbc0">?</text></svg>
  </header>

  <section class="report-card">
    <div class="card-heading">
      <svg width="36" height="32" viewBox="0 0 36 32"><path d="M18 1L35 31H1Z" fill="#e04a4a"/><rect x="16.5" y="11" width="3" height="11" fill="#fff"/><rect x="16.5" y="24.5" width="3" height="3" fill="#fff"/></svg>
      <h1>Report Distruptive Behavior</h1>
    </div>
    <div class="rule"></div>
    <p class="complaint">Loud music in the apartment 18a all night.<br>Can't sleep and I need to study!</p>
    <div class="body-copy">
      <p>Please describe what happened, when it started and how often it repeats. Include the unit number if you know it so our team can follow up quickly.</p>
      <p>Reports are shared only with the management office. Your name stays private unless you choose to share it.</p>
      <p>Quiet hours run from 10 PM to 7 AM every day. Repeated noise after a written notice may lead to further action under the lease.</p>
      <p>For emergencies such as fire, flooding or gas smells, call the front desk right away instead of using this form. We will reply within one business day.</p>
    </div>
    <button class="submit-button" type="button">Submit</button>
  </section>

  <nav class="tab-bar">
    <div class="tab">
      <svg width="30" height="32" viewBox="0 0 30 32"><circle cx="15" cy="10" r="7"/><path d="M3 30c0-7 5-11 12-11s12 4 12 11z"/></svg>
      My Account
    </div>
    <div class="tab">
      <svg width="34" height="30" viewBox="0 0 34 30"><path d="M4 26l14-14"/><path d="M18 12a7 7 0 1 0 9-9l-4 4-3-1-1-3 4-4"/><circle cx="5" cy="25" r="2.5"/></svg>
      Services
    </div>
    <div class="tab">
      <svg width="34" height="32" viewBox="0 0 34 32"><ellipse cx="12" cy="8" rx="9" ry="3.5"/><path d="M3 8v14c0 2 4 3.5 9 3.5M21 8v6"/><path d="M3 13c0 2 4 3.5 9 3.5M3 18c0 2 4 3.5 9 3.5"/><ellipse cx="23" cy="17" rx="9" ry="3.5"/><path d="M14 17v10c0 2 4 3.5 9 3.5s9-1.5 9-3.5V17M14 22c0 2 4 3.5 9 3.5s9-1.5 9-3.5"/></svg>
      Rents
    </div>
    <div class="tab">
      <svg width="32" height="32" viewBox="0 0 32 32"><circle cx="16" cy="16" r="5"/><path d="M16 3v5M16 24v5M3 16h5M24 16h5M6.8 6.8l3.5 3.5M21.7 21.7l3.5 3.5M6.8 25.2l3.5-3.5M21.7 10.3l3.5-3.5"/><circle cx="16" cy="16" r="10"/></svg>
      Settings
    </div>
  </nav>
</main>
</body>
</html>
```